Flyer Valrun Take Away
Zielgruppe
Gastrobetrieb mit Afghanischer Küche. Hauptangebot: Reisgerichte, Teigtaschen und Korma (Currygerichte). ZG: Studenten/Schüller, Ladenbesitzer und Passanten, da es sehr Zentral liegt.
Aufgabenstellung
Flyer für die Neueröffnung

```html
<!DOCTYPE html>
<html lang="de">
<head>
<meta charset="utf-8">
<title>Valrun Take Away – Flyer Neueröffnung</title>
<link rel="stylesheet" href="https://fonts.googleapis.com/css2?family=Staatliches&family=Delius&display=swap">
<style>
  :root {
    --stage: #ffffff;
    --pattern-tint: #e7f0da;
    --pattern-deep: #cfe2b8;
    --chili: #b3231f;
    --ink: #1f1f1f;
    --sand: #f3d39f;
    --paper: #ffffff;
    --leaf: #2f6b34;
    --spice-a: #d98a1c;
    --spice-b: #a8331c;
    --spice-c: #4a2a1a;
  }
  * { box-sizing: border-box; margin: 0; padding: 0; }
  html, body { width: 1200px; height: 686px; overflow: hidden; background: var(--stage); }
  body { position: relative; font-family: "Delius", sans-serif; color: var(--ink); }

  .page {
    position: absolute; top: 49px; width: 404px; height: 573px;
    border: 1px solid #333; overflow: hidden;
    background: linear-gradient(135deg, var(--pattern-tint), var(--pattern-deep) 50%, var(--pattern-tint));
  }
  .page--front { left: 184px; }
  .page--menu { left: 630px; }

  .pattern-fill { position: absolute; inset: 0; }
  .shape { position: absolute; inset: 0; width: 100%; height: 100%; }

  /* Front */
  .brand-card {
    position: absolute; left: 28px; top: 2px; width: 121px; height: 160px;
    background: var(--paper); transform: rotate(-3deg); transform-origin: left top;
    display: flex; flex-direction: column; align-items: center; justify-content: center; gap: 8px;
    box-shadow: 0 1px 3px rgba(0,0,0,.25);
  }
  .brand-card__mark { width: 14px; height: 14px; background: var(--chili); }
  .brand-card__name { font-size: 22px; color: var(--ink); line-height: 1; }
  .brand-card__sub { font-size: 14px; color: var(--ink); line-height: 1; }

  .opening {
    position: absolute; left: 24px; top: 382px; width: 380px;
    transform: rotate(-4deg); transform-origin: left top;
  }
  .opening__headline {
    font-family: "Staatliches", sans-serif; font-size: 30px; letter-spacing: 2px;
    color: var(--chili); line-height: 1; white-space: nowrap;
  }
  .opening__date { color: var(--ink); font-size: 32px; margin-left: 8px; }
  .opening__info {
    margin-top: 8px; width: 360px; text-align: center;
    font-size: 14.5px; line-height: 19px; color: var(--ink);
  }

  /* Menu */
  .menu-section {
    position: absolute; width: 340px;
    transform: rotate(-3.5deg); transform-origin: left top;
    font-size: 8.6px; line-height: 13px;
  }
  .menu-section--evening { left: 31px; top: 72px; }
  .menu-section--lunch { left: 48px; top: 312px; }
  .menu-section--extras { left: 59px; top: 462px; }
  .menu-section__title {
    font-family: "Staatliches", sans-serif; color: var(--chili);
    font-size: 10px; letter-spacing: 1.2px; line-height: 11px;
  }
  .menu-item { margin-bottom: 11px; }
  .menu-section--lunch .menu-item { margin-bottom: 12px; }
  .menu-item__name { font-weight: bold; }
  .menu-item__price { color: var(--chili); }
</style>
</head>
<body>

<section class="page page--front" aria-label="Flyer Vorderseite">
  <div class="pattern-fill" role="img" aria-label="Grünes geometrisches Zickzack-Rautenmuster als Hintergrund"></div>

  <svg class="shape" viewBox="0 0 404 573" aria-hidden="true">
    <polygon points="0,360 404,332 404,484 0,512" fill="#ffffff" opacity="0.92"/>
    <line x1="0" y1="357" x2="352" y2="332" stroke="var(--chili)" stroke-width="2"/>
    <line x1="242" y1="491" x2="404" y2="481" stroke="var(--chili)" stroke-width="2"/>
    <line x1="136" y1="507" x2="404" y2="488" stroke="var(--chili)" stroke-width="2"/>
  </svg>

  <svg class="shape" viewBox="0 0 404 573" role="img" aria-label="Foto: Schalen mit Currypulver, Paprika, rotem Pfeffer und Kräutern auf Holztisch">
    <defs>
      <linearGradient id="spice-photo" x1="0" y1="0" x2="1" y2="1">
        <stop offset="0" stop-color="var(--spice-c)"/>
        <stop offset="0.35" stop-color="var(--spice-a)"/>
        <stop offset="0.7" stop-color="var(--spice-b)"/>
        <stop offset="1" stop-color="var(--spice-c)"/>
      </linearGradient>
    </defs>
    <polygon points="0,45 404,16 404,306 0,335" fill="url(#spice-photo)"/>
  </svg>

  <div class="brand-card">
    <span class="brand-card__mark"></span>
    <span class="brand-card__name">Valrun</span>
    <span class="brand-card__sub">Take Away</span>
  </div>

  <div class="opening">
    <p class="opening__headline">Neueröffnung!<span class="opening__date">02.11.15</span></p>
    <p class="opening__info">
      Lindenhofgasse 7 // 8001 Zürich<br>
      Tel. +41 76 555 01 23 // www.valrun.ch<br>
      Montag – Samstag // 11:00 – 14:00 Mittags-Menü<br>
      18:00 – 22:00 Teigtaschen // Sonntag Ruhetag
    </p>
  </div>
</section>

<section class="page page--menu" aria-label="Flyer Rückseite mit Speisekarte">
  <div class="pattern-fill" role="img" aria-label="Grünes geometrisches Zickzack-Rautenmuster als Hintergrund"></div>

  <svg class="shape" viewBox="0 0 404 573" aria-hidden="true">
    <polygon points="0,63 376,39 392,257 0,286" fill="var(--sand)"/>
    <polygon points="20,303 404,277 404,409 30,436" fill="var(--sand)"/>
    <polygon points="0,452 374,427 379,518 0,546" fill="var(--sand)"/>
  </svg>

  <div class="menu-section menu-section--evening">
    <h2 class="menu-section__title">Hausgemachte Teigtaschen &amp; Kabob (18.00 bis 22.00 Uhr)</h2>
    <p class="menu-item"><span class="menu-item__name">Mantu</span>: gedämpfte Teigtaschen gefüllt mit Rindshackfleisch und Zwiebeln, serviert an Tomaten Sauce mit gelben Erbsen, Gemüse und Minze-Joghurt Sauce <span class="menu-item__price">(CHF 14.00)</span></p>
    <p class="menu-item"><span class="menu-item__name">Ashak</span>: pochierte Teigtaschen gefüllt mit Lauch serviert mit Hackfleisch-Tomaten Sauce und Minze-Joghurt Sauce <span class="menu-item__price">(CHF 14.00)</span></p>
    <p class="menu-item"><span class="menu-item__name">Boloni</span>: gebratene Teigtaschen gefüllt mit Kartoffeln oder Lauch, serviert mit Minze-Joghurt Sauce und Chakni (rassige Chili-Koriander Sauce) <span class="menu-item__price">(CHF 7.00)</span></p>
    <p class="menu-item"><span class="menu-item__name">Sambosa:</span> gebratene Teigtaschen gefüllt mit Kartoffel und Erbsen, serviert mit Minze-Joghurt Sauce dazu Salat und Chakni (rassige Chili-Koriander Sauce), 2 Stk. <span class="menu-item__price">(CHF 8.00)</span></p>
    <p class="menu-item"><span class="menu-item__name">Shami Kabob</span>: Hackfleischspiess serviert mit Salat nach afghanischer Art und frisch gebackenem Tandoori Brot <span class="menu-item__price">(CHF 9.00)</span></p>
  </div>

  <div class="menu-section menu-section--lunch">
    <h2 class="menu-section__title">Mittagsmenü (11.00 bis 14.00 Uhr)</h2>
    <p class="menu-item"><span class="menu-item__name">Korma</span>: Rassiges Fleisch Curry zubereitet mit orientalischen Gewürzmischungen <span class="menu-item__price">(CHF 14.50)</span></p>
    <p class="menu-item"><span class="menu-item__name">Tarkori</span> : Pikant zubereitetes Gemüse mit Tomaten-Sauce <span class="menu-item__price">(CHF 14.50)</span></p>
    <p class="menu-item"><span class="menu-item__name">Chalau / Palau:</span> Afghanisches Festtags- und Nationalgericht mit Basmati-Reis <span class="menu-item__price">(CHF 14.50)</span></p>
    <h2 class="menu-section__title">Suppe</h2>
    <p class="menu-item"><span class="menu-item__name">Shorba</span>: Traditionelle afghanische Suppe dazu Brotscheibe und eine Frucht <span class="menu-item__price">(CHF 13.50)</span></p>
  </div>

  <div class="menu-section menu-section--extras">
    <h2 class="menu-section__title">Tee-Spezialität</h2>
    <p class="menu-item"><span class="menu-item__name">Shirr-Tschai</span>: Milch-Tee nach afghanischer Art mit Kardamom <span class="menu-item__price">(CHF 4.00)</span></p>
    <h2 class="menu-section__title">Süssgebäck</h2>
    <p class="menu-item"><span class="menu-item__name">Root</span> : Afghanisches Süssgebäck mit gemahlenen Mandeln, braunem Zucker und Schwarzkümmel <span class="menu-item__price">(CHF 4.00)</span></p>
  </div>
</section>

</body>
</html>
```